web Design for Architecture and Interior Design Firm

This is a complete redesign of an architecture and interior design firm.( http://www.tqworkshop.com )
We have established a new look-n-feel for them and need to apply it to the new site/new architecture. Wireframes attached with logo and PDF of new brochure.
This will require a quck turn-around. The client is expecting a very modern design with web 2.0 in mind.
Again very quick turn-around! If you cannot commit to a Friday deliverable, do not bid! Must be completed by no later than Friday!

```html
<!DOCTYPE html>
<html lang="en">
<head>
<meta charset="utf-8">
<title>Tessaro Quinn Design Studios</title>
<link href="https://fonts.googleapis.com/css2?family=Arimo:wght@400;700&family=Roboto+Condensed:wght@400;700&family=Yellowtail&display=swap" rel="stylesheet">
<style>
  :root {
    --ink: #222222;
    --text: #333333;
    --brand-red: #c8102e;
    --orange: #ff9900;
    --band-grey: #e6e6e6;
    --line-grey: #cccccc;
    --panel-grey: #ededed;
    --footer-grey: #9a9a9a;
    --footer-text: #6e6e6e;
    --white: #ffffff;
  }
  * { box-sizing: border-box; margin: 0; padding: 0; }
  html, body { width: 968px; height: 1200px; overflow: hidden; }
  body {
    position: relative;
    background: var(--white);
    font-family: "Arimo", Arial, sans-serif;
    color: var(--text);
  }
  .abs { position: absolute; }

  /* Header */
  .brand { left: 34px; top: 56px; }
  .brand-name {
    font-family: "Roboto Condensed", sans-serif;
    font-weight: 700;
    font-size: 44px;
    letter-spacing: 0.5px;
    color: var(--ink);
    line-height: 1;
  }
  .brand-tagline {
    margin: 6px 0 0 105px;
    font-family: "Roboto Condensed", sans-serif;
    font-size: 15px;
    color: #666;
  }
  .nav-main, .nav-utility {
    top: 139px; height: 43px;
    border: 1px solid var(--line-grey);
    border-bottom: none;
    display: flex; align-items: center;
  }
  .nav-main { left: 36px; width: 541px; padding-left: 17px; gap: 30px; }
  .nav-main a { font-size: 17px; font-weight: 700; color: #3a3a3a; text-decoration: none; letter-spacing: 0.2px; }
  .nav-utility { left: 740px; width: 205px; padding-left: 17px; gap: 26px; }
  .nav-utility a { font-size: 13.5px; font-weight: 700; color: var(--ink); text-decoration: none; }

  /* Hero band */
  .hero-band { left: 0; top: 182px; width: 968px; height: 451px; background: var(--band-grey); border-top: 2px solid #d0d0d0; }
  .hero-card { left: 33px; top: 200px; width: 902px; height: 407px; background: var(--white); border-radius: 9px; }
  .hero-photo {
    left: 55px; top: 221px; width: 564px; height: 366px;
    border-radius: 8px 0 0 8px;
    background: linear-gradient(160deg, #f4f2ee 0%, #e4e0d8 45%, #b9b2a6 75%, #7c6d5c 100%);
  }
  .hero-dots { left: 502px; top: 561px; display: flex; gap: 3px; }
  .hero-dots span { width: 16px; height: 16px; border-radius: 50%; background: var(--white); }
  .hero-dots span.is-active { background: #333; }
  .hero-panel {
    left: 619px; top: 221px; width: 297px; height: 366px;
    background: var(--orange);
    border-radius: 0 8px 8px 0;
  }
  .hero-title {
    position: absolute; left: 39px; top: 22px;
    font-family: "Roboto Condensed", sans-serif;
    font-weight: 700; font-size: 47px; line-height: 53.5px;
    color: var(--white);
  }
  .hero-more {
    position: absolute; left: 85px; top: 302px; width: 99px; height: 43px;
    background: var(--white); border-radius: 4px;
    font-size: 12.5px; font-weight: 700; color: var(--ink);
    display: flex; align-items: center; justify-content: center;
  }

  /* Content */
  .content-backdrop {
    left: 0; top: 633px; width: 968px; height: 524px;
    background: linear-gradient(180deg, #f2f2f2 0%, #ffffff 30%, #f6f6f6 100%);
  }
  .intro-title { left: 34px; top: 660px; font-size: 22.5px; color: var(--brand-red); }
  .intro-subtitle { left: 29px; top: 699px; font-size: 17px; color: var(--ink); }
  .intro-copy { left: 31px; top: 724px; width: 580px; font-size: 13.3px; line-height: 20.8px; color: var(--ink); }
  .values-title { left: 36px; top: 856px; font-size: 16.5px; color: var(--brand-red); }
  .values-list { top: 885px; list-style: none; font-size: 13.3px; line-height: 20.8px; color: var(--ink); }
  .values-list li { padding-left: 18px; position: relative; }
  .values-list li::before { content: "\00BB"; position: absolute; left: 0; top: -1px; font-size: 12px; }
  .values-list.col-a { left: 37px; }
  .values-list.col-b { left: 261px; }

  /* Sidebar */
  .sidebar { left: 650px; top: 660px; width: 266px; height: 490px; background: var(--panel-grey); border: 1px solid var(--line-grey); }
  .sidebar-tab {
    left: 663px; top: 651px; width: 237px; height: 47px;
    background: var(--orange);
    color: var(--white);
    font-family: "Roboto Condensed", sans-serif; font-weight: 700; font-size: 23px;
    display: flex; align-items: center; justify-content: center;
  }
  .sidebar-fold { left: 900px; top: 651px; }
  .sidebar-photo {
    left: 668px; top: 701px; width: 231px; height: 296px;
    background: linear-gradient(180deg, #8e9196 0%, #b8b2ad 50%, #c8494a 100%);
  }
  .sidebar-caption {
    left: 668px; top: 1000px; width: 231px; text-align: center;
    font-family: "Yellowtail", cursive; font-size: 20px; line-height: 23px; color: #111;
  }
  .sidebar-links { left: 677px; top: 1060px; list-style: none; font-size: 13.8px; line-height: 22.7px; color: #444; }

  /* Footer */
  .footer { left: 0; top: 1157px; width: 968px; height: 43px; background: var(--footer-grey); }
  .footer p { position: absolute; left: 53px; top: 13px; font-size: 10px; color: var(--footer-text); }
</style>
</head>
<body>

<header>
  <div class="abs brand">
    <div class="brand-name">TESSARO QUINN</div>
    <div class="brand-tagline">people - focused design</div>
  </div>
  <nav class="abs nav-main">
    <a href="#">Our Competitie Eduge</a>
    <a href="#">Services</a>
    <a href="#">Portfolio</a>
    <a href="#">TQDS News</a>
  </nav>
  <nav class="abs nav-utility">
    <a href="#">Contact Us</a>
    <a href="#">Employment</a>
  </nav>
</header>

<section>
  <div class="abs hero-band"></div>
  <div class="abs hero-card"></div>
  <div class="abs hero-photo" role="img" aria-label="Bright modern dining room with glass table, black and wooden chairs and tall windows onto a garden courtyard"></div>
  <div class="abs hero-dots"><span class="is-active"></span><span></span><span></span><span></span><span></span></div>
  <div class="abs hero-panel">
    <h1 class="hero-title">Probably<br>the best<br>artchitectural<br>company<br>in the world</h1>
    <div class="hero-more">MORE</div>
  </div>
</section>

<main>
  <div class="abs content-backdrop" role="img" aria-label="Faint architectural line drawings in the background"></div>
  <h2 class="abs intro-title">Faced with an Office Move, Expansion Or New Building?</h2>
  <h3 class="abs intro-subtitle" style="font-weight:400">Tessaro Quinn Design Studios Makes the Process Predictable</h3>
  <p class="abs intro-copy">When something as important as the very space in which your business lives and works is about to be disrupted, you should be confident you've chosen the right spaceand the best team to ensure a successful project. Rely on Tessaro-Quinn&nbsp; Design Studios to meet your needs and to make the process predictable. You can be assured that your project goals and objectives will be achieved.</p>
  <h3 class="abs values-title" style="font-weight:400">Our Core Values:</h3>
  <ul class="abs values-list col-a">
    <li>Responsive service</li>
    <li>Friendly and fun to work with</li>
    <li>Client oriented focus</li>
    <li>Teamwork</li>
  </ul>
  <ul class="abs values-list col-b">
    <li>Listening &amp; understanding your needs</li>
    <li>Flexibility</li>
    <li>Creative problem solving</li>
    <li>Learning environment and</li>
    <li>knowledge sharing</li>
  </ul>

  <aside>
    <div class="abs sidebar"></div>
    <div class="abs sidebar-tab">Managing Projects</div>
    <svg class="abs sidebar-fold" width="16" height="9" viewBox="0 0 16 9"><polygon points="0,0 16,9 0,9" fill="#8a8a8a"/></svg>
    <div class="abs sidebar-photo" role="img" aria-label="Portrait of the managing principal in a red shirt and tie"></div>
    <p class="abs sidebar-caption">as seen in the harborline<br>Business Journal</p>
    <ol class="abs sidebar-links">
      <li>1. Managing Projects Archive</li>
      <li>2 Recent News &amp; firm Events</li>
      <li>3 Testimonials</li>
    </ol>
  </aside>
</main>

<footer class="abs footer">
  <p>Copyright 2011.Tessaro Quinn Design Studios.</p>
</footer>

</body>
</html>
```